Dr. Marisa Tellen Medical/Chiropractic Business Card

Dr. Tellen is a chiropractor and will require a business card that she uses every single day to book appointments on the back side of the card. Currently the office name goes by Dr. Marisa Tellen. The chiropractic profession is based on the diagnosis and manipulative treatment of misalignments of the joints, especially those of the spinal column, which are held to cause other disorders by affecting the nerves, muscles, and organs. Dr. Marisa Tellen is looking for a contemporary and minimalistic design.

Industry/Entity Type

Medical

Contact Information for Business Card

Name: Dr. Marisa Tellen; Address: 748 Ashcombe Rd North, London, ON N5R 2K9; Phone Number: 519.672.4193; Fax: 519.681.2054; email: marisa.tellen@brevanmail.com

Requirements
Must have
• ability to write multiple appointments date/time on the back of card

```html
<!DOCTYPE html>
<html lang="en">
<head>
<meta charset="utf-8">
<title>Dr. Marisa Tellen – Business Card</title>
<link rel="stylesheet" href="https://fonts.googleapis.com/css2?family=Tinos:wght@400;700&display=swap">
<style>
  :root {
    --stage: #e8e4df;
    --card-top: #3a96b5;
    --card-bottom: #07729a;
    --back-top: #2a86a7;
    --back-bottom: #076f95;
    --ink: #ffffff;
    --ink-soft: #e6f3f8;
    --stripe: #f2f5f6;
  }
  * { box-sizing: border-box; margin: 0; padding: 0; }
  html, body { width: 1200px; height: 871px; overflow: hidden; }
  body {
    background: var(--stage);
    font-family: "Tinos", "Times New Roman", serif;
    color: var(--ink);
  }
  .canvas {
    width: 1200px; height: 871px;
    display: flex; justify-content: center; align-items: center; gap: 80px;
  }
  .card {
    position: relative;
    width: 400px; height: 700px;
    border-radius: 4px;
    box-shadow: 0 10px 30px rgba(0,0,0,.18);
    overflow: hidden;
  }
  /* front */
  .card--front { background: linear-gradient(180deg, var(--card-top) 0%, var(--card-bottom) 100%); }
  .stripe-wide { position: absolute; top: 0; bottom: 0; left: 22px; width: 22px; background: var(--stripe); }
  .stripe-thin { position: absolute; top: 0; bottom: 0; left: 52px; width: 5px; background: var(--stripe); }
  .front-name {
    position: absolute; left: 70px; right: 10px; top: 395px;
    text-align: center; font-size: 40px; font-weight: 400; letter-spacing: .5px;
  }
  .front-name .title { font-weight: 700; }
  .contact {
    position: absolute; left: 70px; right: 10px; top: 530px;
    list-style: none; text-align: center; font-size: 19px; line-height: 26px;
  }
  .contact li { display: flex; justify-content: center; align-items: flex-start; gap: 8px; }
  .contact svg { width: 14px; height: 14px; margin-top: 6px; fill: var(--ink); flex: none; }
  .contact .address { line-height: 24px; margin-top: 6px; }
  /* back */
  .card--back { background: linear-gradient(160deg, var(--back-top) 0%, var(--back-bottom) 100%); padding: 60px 40px 0; }
  .back-title { font-size: 40px; font-weight: 400; text-align: center; letter-spacing: 1px; }
  .schedule { display: flex; justify-content: space-between; margin-top: 40px; }
  .col-head { font-size: 20px; letter-spacing: 2px; text-transform: uppercase; }
  .col--date { width: 180px; }
  .col--time { width: 105px; }
  .col--time .col-head { margin-top: 40px; text-align: center; }
  .slot { border-bottom: 2px solid var(--ink-soft); height: 62px; }
  .col--date .slot:first-child { height: 24px; }
  .col--time .slot:first-child { height: 22px; }
  .reschedule {
    position: absolute; left: 30px; right: 30px; bottom: 70px;
    font-size: 17px; line-height: 24px; text-align: center; color: var(--ink-soft);
  }
</style>
</head>
<body>
<main class="canvas">
  <section class="card card--front" aria-label="Card front">
    <div class="stripe-wide"></div>
    <div class="stripe-thin"></div>
    <h1 class="front-name"><span class="title">Dr.</span> Marisa Tellen</h1>
    <ul class="contact">
      <li><svg viewBox="0 0 16 16" aria-hidden="true"><path d="M5 1h6a1 1 0 0 1 1 1v12a1 1 0 0 1-1 1H5a1 1 0 0 1-1-1V2a1 1 0 0 1 1-1zm.5 1.5v10h5v-10z"/></svg>519.672.4193</li>
      <li><svg viewBox="0 0 16 16" aria-hidden="true"><path d="M1 5c2-3 12-3 14 0l-1 2-3-1V5H5v1L2 7zM3 8h10l1 6H2z"/></svg>519.681.2054</li>
      <li><svg viewBox="0 0 16 16" aria-hidden="true"><path d="M1 4h14v9H1zm1.5 1.2V6l5.5 3.5L13.5 6v-.8L8 8.6z"/></svg>marisa.tellen@brevanmail.com</li>
      <li class="address"><svg viewBox="0 0 16 16" aria-hidden="true"><path d="M8 1l7 6.5h-2V15H9.5v-4h-3v4H3V7.5H1z"/></svg><span>748 Ashcombe Rd North<br>London, ON N5R 2K9</span></li>
    </ul>
  </section>

  <section class="card card--back" aria-label="Card back">
    <h2 class="back-title">Appointments</h2>
    <div class="schedule">
      <div class="col col--date">
        <div class="col-head">Date</div>
        <div class="slot"></div><div class="slot"></div><div class="slot"></div>
        <div class="slot"></div><div class="slot"></div><div class="slot"></div>
      </div>
      <div class="col col--time">
        <div class="col-head">Time</div>
        <div class="slot"></div><div class="slot"></div><div class="slot"></div>
        <div class="slot"></div><div class="slot"></div><div class="slot"></div>
      </div>
    </div>
    <p class="reschedule">If you are unable to make your appointment<br>please call us to reschedule</p>
  </section>
</main>
</body>
</html>
```